ultra-minimalist business card

front (black background, matte):

tarik b. hosseny
writer | photographer
get@tarikhosseny.com

back (white background, matte):

a picture speaks a thousand words;
a word draws a thousand pictures.

www.tarikhosseny.com

all text should be small (white or silver - as long as it shows against the black - on the front; black or gray - as long as it shows against the white - on the back).

feel free to get creative in terms of arrangement, alignment, and font type, but remember, the overall style is minimalist, so nothing too fancy, please.

thanks.

```html
<!DOCTYPE html>
<html lang="en">
<head>
<meta charset="UTF-8">
<title>Tarik B. Hosseny — Business Card Back</title>
<link rel="stylesheet" href="https://fonts.googleapis.com/css2?family=Playfair+Display:wght@700&family=Montserrat:wght@400&display=swap">
<style>
  :root {
    --card-bg: #ffffff;
    --ink: #141414;
    --ink-soft: #222222;
  }
  * { margin: 0; padding: 0; box-sizing: border-box; }
  html, body {
    width: 1200px;
    height: 776px;
    overflow: hidden;
    background: var(--card-bg);
  }
  .card-back {
    position: relative;
    width: 1200px;
    height: 776px;
    background: var(--card-bg);
  }
  .quote {
    position: absolute;
    top: 328px;
    left: 0;
    width: 100%;
    text-align: center;
    font-family: "Playfair Display", Georgia, serif;
    font-weight: 700;
    font-size: 30px;
    line-height: 47px;
    letter-spacing: 0.09em;
    text-transform: uppercase;
    color: var(--ink);
  }
  .quote-line { display: block; }
  .website {
    position: absolute;
    top: 450px;
    left: 0;
    width: 100%;
    text-align: center;
    font-family: "Montserrat", Arial, sans-serif;
    font-weight: 400;
    font-size: 18px;
    letter-spacing: 0.34em;
    color: var(--ink-soft);
  }
</style>
</head>
<body>
  <main class="card-back">
    <p class="quote">
      <span class="quote-line">A picture speaks a thousand words;</span>
      <span class="quote-line">a word draws a thousand pictures.</span>
    </p>
    <p class="website">www.tarikhosseny.com</p>
  </main>
</body>
</html>
```